Real Estate Webpage Design

We have an existing website: verindaleestates.com.au
We focus customised service mainly on Property Management and second-hand property sales.
We are not entirely happy about the current design and layout can stay roughly the same as the back end coding is linked to a CRM system.
We would like to see the design are more reachable to our clients and appearing.
Please check our Website Design Draft for more details.

Industry/Entity Type

Real estate Agency

Number of Pages Required

5+ page

Font styles to use
Sans Serif

Colors

Designer to choose colors to be used in the design.

```html
<!DOCTYPE html>
<html lang="en">
<head>
<meta charset="utf-8">
<title>Verindale — Real Estate</title>
<link href="https://fonts.googleapis.com/css2?family=Poppins:wght@400;500;600;700;800&display=swap" rel="stylesheet">
<style>
:root{
  --orange:#f4a05a;
  --orange-deep:#ef8b3c;
  --navy:#2b3d52;
  --ink:#1d2430;
  --text:#3a3f47;
  --muted:#8a9099;
  --light:#f2f6f8;
  --blue:#3f6d8e;
  --blue-panel:#4b7b9b;
  --white:#ffffff;
  --line:#e3e6ea;
}
*{box-sizing:border-box;margin:0;padding:0}
html,body{width:1200px;height:4758px;overflow:hidden}
body{font-family:"Poppins",sans-serif;color:var(--text);background:var(--white);position:relative}
.abs{position:absolute}
section{position:absolute;left:0;width:1200px}

/* hero */
.hero{top:0;height:663px;background:linear-gradient(180deg,#7f9dbd 0%,#a9b8c6 30%,#8a7a66 62%,#6a5038 100%)}
.brand{left:85px;top:26px;display:flex;align-items:center;gap:10px;color:var(--orange);font-weight:600;font-size:38px;letter-spacing:.5px}
.brand-dot{width:40px;height:40px;border-radius:50%;background:var(--orange)}
.nav{left:495px;top:50px;display:flex;gap:22px;font-size:14px;font-weight:500;color:var(--white)}
.nav .on{color:var(--orange);border-bottom:2px solid var(--orange);padding-bottom:4px}
.hero h1{position:absolute;left:0;width:1200px;top:258px;text-align:center;color:var(--white);font-weight:800;font-size:40px;line-height:63px;letter-spacing:2px}
.search{left:172px;top:390px;width:856px;height:58px;border-radius:29px;background:rgba(255,255,255,.38);display:flex;align-items:center;padding-left:26px}
.field{width:172px;margin-right:0;color:var(--white)}
.field b{display:block;font-size:14px;font-weight:600;color:var(--ink)}
.field span{font-size:10px;color:#eef2f4}
.search .btn{position:absolute;right:8px;top:7px;width:134px;height:44px;border-radius:22px;background:var(--orange);color:var(--white);font-size:14px;font-weight:600;display:flex;align-items:center;justify-content:center;gap:6px}

/* about */
.about{top:663px;height:600px;background:var(--light)}
.about-frame{left:100px;top:90px}
.about h2{left:523px;top:117px;font-size:28px;font-weight:600;color:var(--ink)}
.underline{height:4px;width:84px;background:var(--orange)}
.about p{left:523px;width:600px;font-size:18.5px;line-height:24px;color:var(--ink)}

/* achievements */
.achieve{top:1165px;height:295px;background:var(--navy)}
.achieve h3{position:absolute;width:1200px;top:100px;text-align:center;color:var(--white);font-size:28px;font-weight:600}
.stat{top:150px;width:260px;text-align:center;color:var(--white)}
.stat b{display:block;color:var(--orange);font-size:54px;font-weight:600;line-height:70px}
.stat span{font-size:19px;font-weight:600}

.sec-title{position:absolute;width:1200px;text-align:center;color:var(--ink);font-size:29px;font-weight:600}
.sec-sub{position:absolute;width:1200px;text-align:center;font-size:19px;color:var(--ink)}
.arrow{width:32px;height:32px;border-radius:50%;border:2px solid var(--orange);background:var(--white)}

/* areas */
.area{display:flex;align-items:center;gap:20px;width:240px}
.area .ph{width:100px;height:100px;border-radius:6px}
.area b{display:block;font-size:17px;font-weight:600;color:var(--ink)}
.area span{font-size:16px;color:var(--muted)}

/* properties */
.tabs{top:2143px;left:475px;font-size:16px;color:var(--ink)}
.card{top:2198px;width:248px}
.card .ph{height:150px;position:relative}
.heart{position:absolute;right:8px;top:8px;width:26px;height:26px;border-radius:5px;background:rgba(255,255,255,.7)}
.card .city{margin:18px 0 0 11px;font-size:16px;font-weight:600;color:var(--ink)}
.card .addr{margin:4px 0 0 11px;font-size:13px;color:var(--ink)}
.feat{margin:12px 0 0 11px;display:flex;gap:14px;font-size:12px;color:var(--muted);align-items:center}
.feat i{display:inline-block;width:13px;height:9px;border:1.5px solid var(--muted);border-radius:2px;margin-right:4px;vertical-align:middle}
.card hr{border:0;border-top:1px solid var(--line);margin:12px 0 0}
.price{display:flex;justify-content:space-between;align-items:center;margin:8px 8px 0 11px;font-size:14px;font-weight:600;color:var(--ink)}
.avatar{width:32px;height:32px;border-radius:50%}

/* explore */
.explore{top:2629px;height:580px;background:var(--blue)}
.explore .sec-title{color:var(--white)}
.explore .sec-sub{color:var(--white)}
.tile{top:182px;width:193px;height:282px;display:flex;align-items:flex-end;justify-content:center;padding-bottom:80px;color:var(--white);font-size:17px;font-weight:600}
.tile svg{position:absolute;top:110px;left:71px}

/* blog */
.blog-main{left:83px;top:3410px;width:332px;height:274px;background:linear-gradient(135deg,#e6e2dc,#d9d7d3 60%,#c9c8c6);padding:45px 26px 0}
.meta{font-size:11px;color:var(--text)}
.blog-main h4{font-size:19px;line-height:24px;font-weight:600;color:var(--ink);margin:8px 0}
.blog-main p{font-size:10.5px;line-height:13px;color:var(--text)}
.pill{display:inline-block;margin-top:14px;padding:6px 14px;background:var(--orange);color:var(--white);font-size:11px;border-radius:3px}
.post{width:360px;height:124px;display:flex;gap:9px}
.post .ph{width:125px;height:120px;flex:none}
.post .meta{font-size:9.5px;color:var(--muted)}
.post h5{font-size:12.5px;line-height:15px;font-weight:600;color:var(--ink);margin:4px 0}
.post p{font-size:9.5px;line-height:11.5px;color:var(--muted)}
.post a{display:block;font-size:10px;color:var(--orange);text-decoration:underline;margin-top:10px}

/* contact */
.contact{top:3852px;height:424px;background:var(--light)}
.contact h2{left:83px;top:90px;font-size:30px;line-height:38px;font-weight:600;color:var(--ink)}
.contact p{left:83px;top:182px;width:400px;font-size:18.5px;line-height:24px;color:var(--ink)}
.form{left:588px;top:50px;width:310px;height:318px;background:var(--blue-panel);padding:30px 26px 0 18px}
.input{height:38px;background:var(--white);border-radius:3px;font-size:11px;color:var(--muted);padding:11px 14px;margin-bottom:16px}
.input.tall{height:80px}
.send{display:inline-block;padding:8px 14px;background:var(--orange);color:var(--white);font-size:11px;border-radius:3px}

/* footer */
.footer{top:4365px;height:393px;background:linear-gradient(100deg,#b9d1e0 0%,#dbe7ef 45%,#a9c3d5 100%)}
.foot-panel{left:45px;top:45px;width:1110px;height:308px;background:rgba(244,247,249,.93)}
.fcol{top:48px;font-size:13px;color:var(--ink);line-height:26px}
.fcol h6{font-size:15px;font-weight:500;margin-bottom:8px}
.fcol small{display:flex;gap:10px;align-items:flex-start;font-size:11px;line-height:14px;color:var(--muted);margin-bottom:14px}
.social{display:flex;gap:14px;margin-top:20px}
.social i{width:12px;height:12px;border-radius:50%;background:var(--ink);display:block}
.sub-in{width:200px;height:38px;background:var(--white);border-radius:3px;font-size:11px;color:var(--muted);padding:11px 14px}
.sub-btn{width:40px;height:38px;background:var(--orange);border-radius:3px}
</style>
</head>
<body>

<section class="hero" role="img" aria-label="Rooftop deck with lounge chairs and palm tree at dusk">
  <div class="abs brand"><span class="brand-dot"></span>Verindale</div>
  <nav class="abs nav">
    <span class="on">HOME</span><span>ABOUT US</span><span>LEASING</span><span>BUY</span><span>SELL</span><span>OUR TEAM</span><span>BLOG</span><span>CONTACT US</span>
  </nav>
  <h1>PLAN YOUR FUTURE PROPERTY WITH US,<br>ARE YOU READY ?</h1>
  <div class="abs search">
    <div class="field"><b>TYPE</b><span>Property Type</span></div>
    <div class="field"><b>LOCATION</b><span>All Cities</span></div>
    <div class="field"><b>SEARCH</b><span>Enter Keywords</span></div>
    <div class="btn"><svg width="16" height="16" viewBox="0 0 16 16"><circle cx="7" cy="7" r="5" fill="none" stroke="#fff" stroke-width="2"/><line x1="11" y1="11" x2="15" y2="15" stroke="#fff" stroke-width="2"/></svg>SEARCH</div>
  </div>
</section>

<section class="about">
  <svg class="abs about-frame" width="390" height="345" viewBox="0 0 390 345">
    <polygon points="195,0 390,58 390,345 0,345 0,58" fill="#fff"/>
    <defs><linearGradient id="hands" x1="0" y1="0" x2="1" y2="1"><stop offset="0" stop-color="#e9ebec"/><stop offset=".6" stop-color="#d8d9d8"/><stop offset="1" stop-color="#c9a68c"/></linearGradient></defs>
    <polygon points="195,16 375,68 375,330 15,330 15,68" fill="url(#hands)" role="img" aria-label="Hands holding a small model house"/>
  </svg>
  <h2 class="abs">Verindale</h2>
  <div class="abs underline" style="left:523px;top:160px"></div>
  <p class="abs" style="top:185px">Verindale is built on one idea: a home is one of the most important and valuable assets people will ever own. Verindale is a real estate company located in Gungahlin, Canberra.</p>
  <p class="abs" style="top:307px">Being a portfolio sales agent and property manager, coupled with our high–profile international real estate experience, Verindale is considered a market leader on the cutting edge with deep industry knowledge, ranging from landlord–tenant relationships, residential purchases.</p>
</section>

<section class="achieve">
  <svg class="abs" style="top:-2px;left:0" width="1200" height="72"><polygon points="0,0 1200,0 600,70" fill="var(--light)"/></svg>
  <h3>Our Achievments</h3>
  <div class="abs stat" style="left:303px"><b>2,763</b><span>Propreties Sold</span></div>
  <div class="abs stat" style="left:621px"><b>1,682</b><span>Propreties Leased</span></div>
</section>

<div class="sec-title" style="top:1540px">Areas We Serve</div>
<div class="sec-sub" style="top:1586px">Explore our areas to find your future property</div>
<div class="abs arrow" style="left:41px;top:1744px"></div>
<div class="abs arrow" style="left:1125px;top:1744px"></div>
<div class="abs area" style="left:103px;top:1645px"><div class="ph" style="background:linear-gradient(#2a2f4a,#6b4a3a)" role="img" aria-label="Canberra at night"></div><div><b>Canberra</b><span>24 Listings</span></div></div>
<div class="abs area" style="left:365px;top:1645px"><div class="ph" style="background:linear-gradient(#9ab9d6,#8b8f96)" role="img" aria-label="Newcastle bridge"></div><div><b>Newcastle</b><span>24 Listings</span></div></div>
<div class="abs area" style="left:628px;top:1645px"><div class="ph" style="background:linear-gradient(#c26a3a,#2b2320)" role="img" aria-label="Los Angeles palms at sunset"></div><div><b>Los Angeles</b><span>24 Listings</span></div></div>
<div class="abs area" style="left:890px;top:1645px"><div class="ph" style="background:linear-gradient(#9fc7e4,#dfe7ee)" role="img" aria-label="Paris tower"></div><div><b>Paris</b><span>24 Listings</span></div></div>
<div class="abs area" style="left:103px;top:1778px"><div class="ph" style="background:linear-gradient(#b7cde0,#7b7f86)" role="img" aria-label="Melbourne towers"></div><div><b>Melbourne</b><span>24 Listings</span></div></div>
<div class="abs area" style="left:365px;top:1778px"><div class="ph" style="background:linear-gradient(#d8c8c8,#9c3a3a)" role="img" aria-label="London street with bus"></div><div><b>London</b><span>24 Listings</span></div></div>
<div class="abs area" style="left:628px;top:1778px"><div class="ph" style="background:linear-gradient(#dcc6a5,#4a6b7c)" role="img" aria-label="Auckland skyline over water"></div><div><b>Auckland</b><span>24 Listings</span></div></div>
<div class="abs area" style="left:890px;top:1778px"><div class="ph" style="background:linear-gradient(#a9c9e6,#556070)" role="img" aria-label="Miami towers from below"></div><div><b>Miami</b><span>24 Listings</span></div></div>

<div class="sec-title" style="top:2040px">Our Lates Properties</div>
<div class="sec-sub" style="top:2086px">Lorem ipsum dolor sit amet, consectetur adipiscing elit.</div>
<div class="abs tabs">FOR SALE<span style="margin-left:80px;display:inline-block;border-bottom:3px solid var(--orange);padding-bottom:4px">FOR LEASE</span></div>
<div class="abs arrow" style="left:41px;top:2352px"></div>
<div class="abs arrow" style="left:1125px;top:2352px"></div>

<div class="abs card" style="left:81px"><div class="ph" style="background:linear-gradient(#e6e3dc,#b9a58e)" role="img" aria-label="Bright living room"><span class="heart"></span></div><div class="city">Canberra</div><div class="addr">14 Marlow Street Red Hill</div><div class="feat"><span><i></i>2</span><span><i></i>2</span><span><i></i>2</span><span><i></i>800 Sqm</span></div><hr><div class="price">$379,8/mo<span class="avatar" style="background:#7a9bb5"></span></div></div>
<div class="abs card" style="left:345px"><div class="ph" style="background:linear-gradient(#d9d9d7,#7b7670)" role="img" aria-label="Grey modern lounge"><span class="heart"></span></div><div class="city">Melbourne</div><div class="addr">3/8 Kettle Lane</div><div class="feat"><span><i></i>2</span><span><i></i>2</span><span><i></i>2</span><span><i></i>910 Sqm</span></div><hr><div class="price">$431,3/mo<span class="avatar" style="background:#3a3a3a"></span></div></div>
<div class="abs card" style="left:608px"><div class="ph" style="background:linear-gradient(#f1f2f2,#b9bdbf)" role="img" aria-label="White modern house"><span class="heart"></span></div><div class="city">Miami</div><div class="addr">NW 41st Ave</div><div class="feat"><span><i></i>3</span><span><i></i>5</span><span><i></i>2</span><span><i></i>2100 Sqm</span></div><hr><div class="price">$1429,8/mo<span class="avatar" style="background:#b08b78"></span></div></div>
<div class="abs card" style="left:871px"><div class="ph" style="background:linear-gradient(#9fc0de,#6f8a5a)" role="img" aria-label="Large family house with lawn"><span class="heart"></span></div><div class="city">Auckland</div><div class="addr">62 Brookvale Rd</div><div class="feat"><span><i></i>3</span><span><i></i>2</span><span><i></i>2</span><span><i></i>1800 Sqm</span></div><hr><div class="price">$1352,7/mo<span class="avatar" style="background:#5d7a4e"></span></div></div>

<section class="explore" role="img" aria-label="Blue painted brick wall background">
  <div class="sec-title" style="top:68px">Explore Our Properties</div>
  <div class="sec-sub" style="top:112px">Lorem ipsum dolor sit amet, consectetur adipiscing elit.</div>
  <div class="abs arrow" style="left:41px;top:306px"></div>
  <div class="abs arrow" style="left:1125px;top:306px"></div>
  <div class="abs tile" style="left:83px;background:linear-gradient(#8aa6c4,#59616a)" aria-label="Suburban house">House</div>
  <div class="abs tile" style="left:293px;background:linear-gradient(#b8b2a8,#9a5a36)" aria-label="Room with leather sofa">Room</div>
  <div class="abs tile" style="left:503px;background:linear-gradient(#7f8790,#3e4148)" aria-label="Modern villa">Villa</div>
  <div class="abs tile" style="left:713px;background:linear-gradient(#6d737a,#2f3236)" aria-label="Apartment tower">Apartment</div>
  <div class="abs tile" style="left:923px;background:linear-gradient(#8d8c88,#3b3936)" aria-label="Office interior">Office</div>
</section>

<div class="sec-title" style="top:3305px">From Our Blog</div>
<div class="sec-sub" style="top:3351px">Lorem ipsum dolor sit amet, consectetur adipiscing elit.</div>
<div class="abs blog-main" role="img" aria-label="Desk with laptop and coffee">
  <div class="meta">Tom Reyes . 24 May . 3 min read</div>
  <h4>How Long Does It Take<br>to Find a Tenant ?</h4>
  <p>Lorem ipsum dolor sit amet, consectetur adipiscing elit. Morbi eget ultricies sed amet amet elementum faucibus lorem. Enim et massa volutpat at nulla tincidunt suspendisse integer massa.</p>
  <span class="pill">Read More</span>
</div>
<div class="abs post" style="left:433px;top:3410px"><div class="ph" style="background:linear-gradient(#d9d4cc,#b03a2e)" role="img" aria-label="Key beside small red house model"></div><div><div class="meta">Ivan Holt . 08 May . 3 min read</div><h5>For Protect Your Property</h5><p>Lorem ipsum dolor sit amet, consect adipiscing elit. Augue vel lectus mol massa id lectus.</p><a>Read More</a></div></div>
<div class="abs post" style="left:785px;top:3410px"><div class="ph" style="background:linear-gradient(#c7d3dd,#2f3c4c)" role="img" aria-label="Couple reviewing papers"></div><div><div class="meta">Lena Park . 05 May . 3 min read</div><h5>What You Should Know Before Start Renting ?</h5><p>Lorem ipsum dolor sit amet, consect adipiscing elit. Augue vel lectus mol massa id lectus.</p><a>Read More</a></div></div>
<div class="abs post" style="left:433px;top:3560px"><div class="ph" style="background:linear-gradient(#cfd6dc,#d8692e)" role="img" aria-label="People at a meeting table"></div><div><div class="meta">Nora Bell . 17 May . 3 min read</div><h5>Increase Your Housing Project Sales 3x Faster!</h5><p>Lorem ipsum dolor sit amet, consect adipiscing elit. Augue vel lectus mol massa id lectus.</p><a>Read More</a></div></div>
<div class="abs post" style="left:785px;top:3560px"><div class="ph" style="background:linear-gradient(#2f3a40,#b59452)" role="img" aria-label="Renovated interior doorway"></div><div><div class="meta">Lena Park . 05 May . 3 min read</div><h5>Renovating an Existing Home instead of Buying a New House</h5><p>Lorem ipsum dolor sit amet, consect adipiscing elit. Augue vel lectus mol massa id lectus.</p><a>Read More</a></div></div>

<section class="contact">
  <div class="abs" style="left:772px;top:0;width:428px;height:424px;background:linear-gradient(135deg,#e7dcd0,#f1ebe3 50%,#c8743a 85%,#b8b4ae)" role="img" aria-label="Living room with orange armchair and plant"></div>
  <h2 class="abs">We Help You Buy or Sell<br>Your Property</h2>
  <p class="abs">Lorem ipsum dolor sit amet, consectetur adipiscing elit. Commodo mattis feugiat morbi gravida. Consequat aliquet sitvitae quam lacus nulla cras vulputate. Leo quis egestas ultrices morbi nunc, eu.</p>
  <div class="abs form">
    <div class="input">Your Name</div>
    <div class="input">E-mail/Phone</div>
    <div class="input tall">Message</div>
    <span class="send">Send Message</span>
  </div>
</section>

<section class="footer" role="img" aria-label="Glass building facade">
  <div class="abs foot-panel">
    <div class="abs fcol" style="left:32px;width:200px">
      <h6>About</h6>
      <small><svg width="10" height="13" viewBox="0 0 10 13"><path d="M5 12C2 8 1 6 1 4.5a4 4 0 0 1 8 0C9 6 8 8 5 12z" fill="none" stroke="#8a9099"/></svg>18 Harlow Crescent,<br>Gungahlin, ACT, 2912</small>
      <small><svg width="11" height="11" viewBox="0 0 11 11"><path d="M2 1l2 0 1 3-1.5 1a6 6 0 0 0 2.5 2.5L7 6l3 1v2a1 1 0 0 1-1 1A8 8 0 0 1 1 2a1 1 0 0 1 1-1z" fill="none" stroke="#8a9099"/></svg>02 6190 4410</small>
      <small><svg width="12" height="9" viewBox="0 0 12 9"><rect x=".5" y=".5" width="11" height="8" fill="none" stroke="#8a9099"/><path d="M.5.5 6 5l5.5-4.5" fill="none" stroke="#8a9099"/></svg>hello@verindaleestates.com.au</small>
      <div class="social"><i></i><i></i><i></i><i></i></div>
    </div>
    <div class="abs fcol" style="left:375px"><h6>Discover</h6>Canberra<br>Melbourne<br>Perth<br>Newcastle</div>
    <div class="abs fcol" style="left:495px"><h6>Lists by Category</h6>House<br>Room<br>Apartment<br>Villa<br>Office</div>
    <div class="abs fcol" style="left:673px"><h6>Quick Access</h6>About Us<br>Leasing<br>Buy<br>Sell<br>Our Team<br>Blog</div>
    <div class="abs fcol" style="left:815px"><h6>Subscribe</h6>
      <div style="display:flex;gap:14px"><div class="sub-in">Your E-mail</div><div class="sub-btn"></div></div>
    </div>
  </div>
</section>

</body>
</html>
```